v eLiquid Label

We are an electronic cigarette eLiquid manufacturer with an outdated label design which needs to be updated and become more modern. All information listed on the label cannot be changed or removed.

There are 4 colour coding on the labels that cannot change.
0mg is white
12mg is yellow
18mg is blue
24mg is red

We prefer a blue type background however are not committed to it with the proper design however if a new colour is chosen it must compliment the colour band for each colour coding

The "dots" on the front of the bottle need to be larger.

The "V" on the front needs to be in this font however we can accept slight changes to it for effect.

Issues we are facing:
The 0mg and the 18mg look too close in colour and need to be completely different in colouring.

The background colouring is too dark and you cannot see the 50/50 in the watermark.

Reason: We have not received a design which is suitable to our needs. We have see a few close ones however not exact. Thanks

Reason: I was forced to go out of country for a family emergency and to be fair I am extending the deadline

```html
<!DOCTYPE html>
<html lang="en">
<head>
<meta charset="utf-8">
<title>Kestrel E-Liquid – 30 ml bottle labels</title>
<link rel="stylesheet" href="https://fonts.googleapis.com/css2?family=Oswald:wght@500;600;700&family=Arimo:wght@400;700&display=swap">
<style>
  :root{
    --ink:#111;
    --paper:#fff;
    --label-blue:#5aaac7;
    --panel-blue:#7dbfd6;
    --zero-band:#ffffff;
    --yellow:#f6ea2f;
    --navy:#2b2a7a;
    --red:#e62a2c;
    --heading:"Oswald", "Arial Narrow", sans-serif;
    --body:"Arimo", Arial, sans-serif;
  }
  *{box-sizing:border-box;margin:0;padding:0}
  html,body{width:1200px;height:900px;overflow:hidden;background:var(--paper)}
  body{position:relative;font-family:var(--body)}

  .label{
    position:absolute;width:878px;height:343px;
    border:1.5px solid var(--ink);background:var(--label-blue);
    transform-origin:0 0;overflow:hidden;
    --band-bg:var(--zero-band);--band-fg:var(--ink);
    --dot-bg:#fff;--dot-fg:#444;
  }
  .label--small{transform:scale(.6663)}
  .label--zero-a{left:13px;top:33px}
  .label--12{left:611px;top:33px;--band-bg:var(--yellow);--dot-bg:var(--yellow);--dot-fg:var(--ink)}
  .label--18{left:13px;top:283px;--band-bg:var(--navy);--band-fg:#fff;--dot-bg:var(--navy);--dot-fg:#fff}
  .label--24{left:611px;top:283px;--band-bg:var(--red);--band-fg:#fff;--dot-bg:var(--red);--dot-fg:#fff}
  .label--zero-b{left:163px;top:532px}

  .band{
    position:absolute;left:0;right:0;height:34px;padding:0 6px;
    background:var(--band-bg);color:var(--band-fg);
    display:flex;justify-content:space-evenly;align-items:center;
    font:700 12.5px/1 var(--body);letter-spacing:4px;white-space:nowrap;
  }
  .band--top{top:0;border-bottom:1.5px solid var(--ink)}
  .band--bottom{bottom:0;border-top:1.5px solid var(--ink)}

  .pattern{
    position:absolute;left:222px;right:0;top:34px;bottom:34px;
    background:
      radial-gradient(ellipse 160px 220px at 120px 90px, rgba(142,203,224,.55), transparent 70%),
      radial-gradient(ellipse 200px 160px at 520px 260px, rgba(142,203,224,.4), transparent 70%),
      linear-gradient(90deg, var(--label-blue), #62b0cb);
  }
  .panel{
    position:absolute;left:0;width:222px;top:34px;bottom:34px;
    background:var(--panel-blue);color:#fff;
  }
  .ingredients__title{
    position:absolute;left:17px;top:26px;
    font:600 19px/1 var(--heading);color:var(--ink);text-transform:uppercase;
  }
  .ingredients__ratio{
    position:absolute;left:135px;top:26px;
    font:600 19px/1 var(--heading);color:var(--ink);white-space:nowrap;
  }
  .ingredients__ratio small{font-size:10px}
  .ingredients__list{position:absolute;left:17px;top:58px;width:200px;font:700 10px/1.3 var(--body)}
  .ingredients__list p+p{margin-top:5px}
  .producer{position:absolute;left:22px;top:152px;width:190px}
  .producer__note{font:700 8px/1.7 var(--body);color:var(--ink);padding-left:30px}
  .producer__address{font:700 10.5px/1.3 var(--body);color:#fff;margin-top:3px}
  .batch{
    position:absolute;left:20px;top:215px;width:182px;height:37px;
    background:#fff;color:var(--ink);font:400 10px/1.2 var(--body);padding:5px 8px;
  }

  .dot{
    position:absolute;left:260px;top:86px;width:94px;height:94px;border-radius:50%;
    background:var(--dot-bg);border:5px solid #cfd3d6;
    box-shadow:0 0 0 2px var(--ink);
    display:flex;align-items:center;justify-content:center;
    font:700 32px/1 var(--heading);color:var(--dot-fg);
  }
  .dot--zero{font-size:28px}

  .brand{position:absolute;left:372px;top:104px;font:700 46px/1 var(--heading);color:var(--ink);text-transform:uppercase;letter-spacing:1px}
  .product{position:absolute;left:440px;top:218px;font:700 32px/1 var(--heading);color:var(--ink);text-transform:uppercase}
  .volume{position:absolute;left:530px;top:188px;font:600 18px/1 var(--heading);color:var(--ink)}
  .blank{position:absolute;left:579px;top:104px;width:75px;height:149px;background:#fff}

  .hazard-icon{position:absolute;left:336px;top:285px;width:22px;height:22px}

  .warnings{position:absolute;left:666px;top:0;width:202px;height:100%;color:#fff}
  .warnings h3{position:absolute;left:0;right:0;font:600 16px/1 var(--heading);color:var(--ink);text-transform:uppercase;white-space:nowrap;letter-spacing:-.2px}
  .warnings h3.right{text-align:right}
  .warnings p{position:absolute;left:0;right:0;font:700 10px/14px var(--body);text-align:justify}
  .w-h1{top:42px}.w-p1{top:62px}
  .w-h2{top:124px}.w-p2{top:144px}
  .w-h3{top:193px}.w-p3{top:213px}
</style>
</head>
<body>

<!-- ZERO (small) -->
<section class="label label--small label--zero-a">
  <div class="band band--top"><span>NICOTINE FREE</span><span>NICOTINE FREE</span><span>NICOTINE FREE</span><span>NICOTINE FREE</span><span>NICOTINE FREE</span></div>
  <div class="pattern" role="img" aria-label="Faint large outlined letter marks in pale blue"></div>
  <div class="panel">
    <h2 class="ingredients__title">Ingrédients</h2>
    <div class="ingredients__ratio">50<small>PG</small> - 50<small>VG</small></div>
    <div class="ingredients__list">
      <p>Propylène Glycol, Glycérine, Alcool de Qualitié Alimentaire, Arômes Naturel et Artificiels</p>
      <p>Propylene Glycol, Vegetable Glycerine, Food Grade Alcohol, Natural and Artificial Flavours.</p>
    </div>
    <div class="producer"><p class="producer__note">Produit et emballé exclusivement pour:<br>Produced and Packaged Exclusively for:</p><p class="producer__address">4419273 Ontario Ltd, Millbrook ON,<br>K0L 1N0</p></div>
    <div class="batch">BATCH:<br>EXPIRES:</div>
  </div>
  <div class="dot dot--zero">Zero</div>
  <div class="brand">Kestrel</div>
  <div class="volume">30 ML</div>
  <div class="product">E-Liquid</div>
  <div class="blank"></div>
  <svg class="hazard-icon" viewBox="0 0 22 22" aria-hidden="true"><polygon points="7,1 15,1 21,7 21,15 15,21 7,21 1,15 1,7" fill="none" stroke="#111" stroke-width="2"/><path d="M7 7l8 8M15 7l-8 8" stroke="#111" stroke-width="2"/></svg>
  <div class="warnings">
    <h3 class="right w-h1">Contenir nocif</h3>
    <p class="w-p1">Ne pas avaler. Ne pas mettre dans les yeux ou sur la peau ou les vêtements. Tenis hors de portée des enfants et des animaux.</p>
    <h3 class="w-h2">Warning contents harmful</h3>
    <p class="w-p2">Do not swallow. Do not get in eyes or on skin or clothing. Keep out of reach of children and pets.</p>
    <h3 class="right w-h3">Danger poison</h3>
    <p class="w-p3">En cas d'ingestion consulter centre antipoison ou un médecin immédiatement. Peux contenir de noix.<br>If swallowed consult poison control centre or a doctor immediately. May contain nuts.</p>
  </div>
  <div class="band band--bottom"><span>ZÉRO NICOTINE</span><span>ZÉRO NICOTINE</span><span>ZÉRO NICOTINE</span><span>ZÉRO NICOTINE</span><span>ZÉRO NICOTINE</span></div>
</section>

<!-- 12 mg -->
<section class="label label--small label--12">
  <div class="band band--top"><span>12mg/ml</span><span>12mg/ml</span><span>12mg/ml</span><span>12mg/ml</span><span>12mg/ml</span><span>12mg/ml</span><span>12mg/ml</span></div>
  <div class="pattern" role="img" aria-label="Faint large outlined letter marks in pale blue"></div>
  <div class="panel">
    <h2 class="ingredients__title">Ingrédients</h2>
    <div class="ingredients__ratio">50<small>PG</small> - 50<small>VG</small></div>
    <div class="ingredients__list">
      <p>Propylène Glycol, Glycérine, Alcool de Qualitié Alimentaire, Arômes Naturel et Artificiels, Nicotine (1.2%)</p>
      <p>Propylene Glycol, Vegetable Glycerine, Food Grade Alcohol, Natural and Artificial Flavours, Nicotine (1.2%)</p>
    </div>
    <div class="producer"><p class="producer__note">Produit et emballé exclusivement pour:<br>Produced and Packaged Exclusively for:</p><p class="producer__address">4419273 Ontario Ltd, Millbrook ON,<br>K0L 1N0</p></div>
    <div class="batch">BATCH:<br>EXPIRES:</div>
  </div>
  <div class="dot">12</div>
  <div class="brand">Kestrel</div>
  <div class="volume">30 ML</div>
  <div class="product">E-Liquid</div>
  <div class="blank"></div>
  <svg class="hazard-icon" viewBox="0 0 22 22" aria-hidden="true"><polygon points="7,1 15,1 21,7 21,15 15,21 7,21 1,15 1,7" fill="none" stroke="#111" stroke-width="2"/><path d="M7 7l8 8M15 7l-8 8" stroke="#111" stroke-width="2"/></svg>
  <div class="warnings">
    <h3 class="right w-h1">Contenir nocif</h3>
    <p class="w-p1">Ne pas avaler. Ne pas mettre dans les yeux ou sur la peau ou les vêtements. Tenis hors de portée des enfants et des animaux.</p>
    <h3 class="w-h2">Warning contents harmful</h3>
    <p class="w-p2">Do not swallow. Do not get in eyes or on skin or clothing. Keep out of reach of children and pets.</p>
    <h3 class="right w-h3">Danger poison</h3>
    <p class="w-p3">En cas d'ingestion consulter centre antipoison ou un médecin immédiatement. Peux contenir de noix.<br>If swallowed consult poison control centre or a doctor immediately. May contain nuts.</p>
  </div>
  <div class="band band--bottom"><span>DANGER POISON</span><span>DANGER POISON</span><span>DANGER POISON</span><span>DANGER POISON</span><span>DANGER POISON</span></div>
</section>

<!-- 18 mg -->
<section class="label label--small label--18">
  <div class="band band--top"><span>18mg/ml</span><span>18mg/ml</span><span>18mg/ml</span><span>18mg/ml</span><span>18mg/ml</span><span>18mg/ml</span><span>18mg/ml</span></div>
  <div class="pattern" role="img" aria-label="Faint large outlined letter marks in pale blue"></div>
  <div class="panel">
    <h2 class="ingredients__title">Ingrédients</h2>
    <div class="ingredients__ratio">50<small>PG</small> - 50<small>VG</small></div>
    <div class="ingredients__list">
      <p>Propylène Glycol, Glycérine, Alcool de Qualitié Alimentaire, Arômes Naturel et Artificiels, Nicotine (1.8%)</p>
      <p>Propylene Glycol, Vegetable Glycerine, Food Grade Alcohol, Natural and Artificial Flavours, Nicotine (1.8%)</p>
    </div>
    <div class="producer"><p class="producer__note">Produit et emballé exclusivement pour:<br>Produced and Packaged Exclusively for:</p><p class="producer__address">4419273 Ontario Ltd, Millbrook ON,<br>K0L 1N0</p></div>
    <div class="batch">BATCH:<br>EXPIRES:</div>
  </div>
  <div class="dot">18</div>
  <div class="brand">Kestrel</div>
  <div class="volume">30 ML</div>
  <div class="product">E-Liquid</div>
  <div class="blank"></div>
  <svg class="hazard-icon" viewBox="0 0 22 22" aria-hidden="true"><polygon points="7,1 15,1 21,7 21,15 15,21 7,21 1,15 1,7" fill="none" stroke="#111" stroke-width="2"/><path d="M7 7l8 8M15 7l-8 8" stroke="#111" stroke-width="2"/></svg>
  <div class="warnings">
    <h3 class="right w-h1">Contenir nocif</h3>
    <p class="w-p1">Ne pas avaler. Ne pas mettre dans les yeux ou sur la peau ou les vêtements. Tenis hors de portée des enfants et des animaux.</p>
    <h3 class="w-h2">Warning contents harmful</h3>
    <p class="w-p2">Do not swallow. Do not get in eyes or on skin or clothing. Keep out of reach of children and pets.</p>
    <h3 class="right w-h3">Danger poison</h3>
    <p class="w-p3">En cas d'ingestion consulter centre antipoison ou un médecin immédiatement. Peux contenir de noix.<br>If swallowed consult poison control centre or a doctor immediately. May contain nuts.</p>
  </div>
  <div class="band band--bottom"><span>DANGER POISON</span><span>DANGER POISON</span><span>DANGER POISON</span><span>DANGER POISON</span><span>DANGER POISON</span></div>
</section>

<!-- 24 mg -->
<section class="label label--small label--24">
  <div class="band band--top"><span>24mg/ml</span><span>24mg/ml</span><span>24mg/ml</span><span>24mg/ml</span><span>24mg/ml</span><span>24mg/ml</span><span>24mg/ml</span></div>
  <div class="pattern" role="img" aria-label="Faint large outlined letter marks in pale blue"></div>
  <div class="panel">
    <h2 class="ingredients__title">Ingrédients</h2>
    <div class="ingredients__ratio">50<small>PG</small> - 50<small>VG</small></div>
    <div class="ingredients__list">
      <p>Propylène Glycol, Glycérine, Alcool de Qualitié Alimentaire, Arômes Naturel et Artificiels, Nicotine (2.4%)</p>
      <p>Propylene Glycol, Vegetable Glycerine, Food Grade Alcohol, Natural and Artificial Flavours, Nicotine (2.4%)</p>
    </div>
    <div class="producer"><p class="producer__note">Produit et emballé exclusivement pour:<br>Produced and Packaged Exclusively for:</p><p class="producer__address">4419273 Ontario Ltd, Millbrook ON,<br>K0L 1N0</p></div>
    <div class="batch">BATCH:<br>EXPIRES:</div>
  </div>
  <div class="dot">24</div>
  <div class="brand">Kestrel</div>
  <div class="volume">30 ML</div>
  <div class="product">E-Liquid</div>
  <div class="blank"></div>
  <svg class="hazard-icon" viewBox="0 0 22 22" aria-hidden="true"><polygon points="7,1 15,1 21,7 21,15 15,21 7,21 1,15 1,7" fill="none" stroke="#111" stroke-width="2"/><path d="M7 7l8 8M15 7l-8 8" stroke="#111" stroke-width="2"/></svg>
  <div class="warnings">
    <h3 class="right w-h1">Contenir nocif</h3>
    <p class="w-p1">Ne pas avaler. Ne pas mettre dans les yeux ou sur la peau ou les vêtements. Tenis hors de portée des enfants et des animaux.</p>
    <h3 class="w-h2">Warning contents harmful</h3>
    <p class="w-p2">Do not swallow. Do not get in eyes or on skin or clothing. Keep out of reach of children and pets.</p>
    <h3 class="right w-h3">Danger poison</h3>
    <p class="w-p3">En cas d'ingestion consulter centre antipoison ou un médecin immédiatement. Peux contenir de noix.<br>If swallowed consult poison control centre or a doctor immediately. May contain nuts.</p>
  </div>
  <div class="band band--bottom"><span>DANGER POISON</span><span>DANGER POISON</span><span>DANGER POISON</span><span>DANGER POISON</span><span>DANGER POISON</span></div>
</section>

<!-- ZERO (full size) -->
<section class="label label--zero-b">
  <div class="band band--top"><span>NICOTINE FREE</span><span>NICOTINE FREE</span><span>NICOTINE FREE</span><span>NICOTINE FREE</span><span>NICOTINE FREE</span></div>
  <div class="pattern" role="img" aria-label="Faint large outlined letter marks in pale blue"></div>
  <div class="panel">
    <h2 class="ingredients__title">Ingrédients</h2>
    <div class="ingredients__ratio">50<small>PG</small> - 50<small>VG</small></div>
    <div class="ingredients__list">
      <p>Propylène Glycol, Glycérine, Alcool de Qualitié Alimentaire, Arômes Naturel et Artificiels</p>
      <p>Propylene Glycol, Vegetable Glycerine, Food Grade Alcohol, Natural and Artificial Flavours.</p>
    </div>
    <div class="producer"><p class="producer__note">Produit et emballé exclusivement pour:<br>Produced and Packaged Exclusively for:</p><p class="producer__address">4419273 Ontario Ltd, Millbrook ON,<br>K0L 1N0</p></div>
    <div class="batch">BATCH:<br>EXPIRES:</div>
  </div>
  <div class="dot dot--zero">Zero</div>
  <div class="brand">Kestrel</div>
  <div class="volume">30 ML</div>
  <div class="product">E-Liquid</div>
  <div class="blank"></div>
  <svg class="hazard-icon" viewBox="0 0 22 22" aria-hidden="true"><polygon points="7,1 15,1 21,7 21,15 15,21 7,21 1,15 1,7" fill="none" stroke="#111" stroke-width="2"/><path d="M7 7l8 8M15 7l-8 8" stroke="#111" stroke-width="2"/></svg>
  <div class="warnings">
    <h3 class="right w-h1">Contenir nocif</h3>
    <p class="w-p1">Ne pas avaler. Ne pas mettre dans les yeux ou sur la peau ou les vêtements. Tenis hors de portée des enfants et des animaux.</p>
    <h3 class="w-h2">Warning contents harmful</h3>
    <p class="w-p2">Do not swallow. Do not get in eyes or on skin or clothing. Keep out of reach of children and pets.</p>
    <h3 class="right w-h3">Danger poison</h3>
    <p class="w-p3">En cas d'ingestion consulter centre antipoison ou un médecin immédiatement. Peux contenir de noix.<br>If swallowed consult poison control centre or a doctor immediately. May contain nuts.</p>
  </div>
  <div class="band band--bottom"><span>ZÉRO NICOTINE</span><span>ZÉRO NICOTINE</span><span>ZÉRO NICOTINE</span><span>ZÉRO NICOTINE</span><span>ZÉRO NICOTINE</span></div>
</section>

</body>
</html>
```